Social Media Graphics - ALL TEXT RK

We are looking for a series of social media graphics for Instagram (standard size 1:1 (1080x1080px) that are ALL TEXT. We want the following quotes below on each graphic; one quote per graphic. AND, In very small letters at the bottom of each graphic, add @RKMarlowLive

The look and feel of these graphics should be complimentary to the color palette attached below; but keep them simple. But the design is up to you; at the end of this document, I provided various samples of all text graphics that I like as examples.

Target Market(s)

women looking to lose weight

Industry/Entity Type

health and wellness

Colors
E54698
E96AAD
F1A4CE
F9D9EA
FCEFF6

Requirements
Must have
• the quotes in the document
Should not have
• no stock photography

```html
<!DOCTYPE html>
<html lang="en">
<head>
<meta charset="utf-8">
<title>RK Social Graphics Series</title>
<link href="https://fonts.googleapis.com/css2?family=Anton&family=Josefin+Sans:wght@600;700&family=Poppins:wght@600&display=swap" rel="stylesheet">
<style>
:root{
  --plum:#672146;
  --rose:#e54698;
  --rose-mid:#e96aad;
  --rose-soft:#f1a4ce;
  --blush:#f9d9ea;
  --mist:#fceff6;
  --white:#ffffff;
}
*{margin:0;padding:0;box-sizing:border-box}
html,body{width:1200px;height:2795px;overflow:hidden;background:var(--plum)}
.board{position:relative;width:1200px;height:2795px}
.tile{
  position:absolute;width:498px;height:498px;overflow:hidden;
  background:linear-gradient(120deg,#dc4d97 0%,#e65ea6 45%,#f07ab9 75%,#e75aa3 100%);
  color:var(--white);text-align:center;
  text-shadow:0 2px 3px rgba(120,20,70,.35);
  display:flex;flex-direction:column;align-items:center;justify-content:center;
  padding:90px 30px 30px;
}
.tile::before{
  content:"";position:absolute;left:44px;right:44px;top:60px;bottom:-200px;
  border-radius:50%;background:rgba(200,50,130,.28);
}
.tile::after{
  content:"";position:absolute;left:0;right:0;bottom:0;height:11px;background:var(--blush);
}
.tile > *{position:relative;z-index:1}
.tab{position:absolute;top:0;left:125px;width:248px;height:19px;background:var(--blush);border-radius:0 0 12px 12px;z-index:1}
.handle{
  position:absolute;top:34px;left:50%;transform:translateX(-50%);
  width:240px;height:44px;border:3px solid var(--white);border-radius:22px;
  font:600 20px/38px "Poppins",sans-serif;text-shadow:none;
}
.col-a{left:86px}.col-b{left:616px}
.row-1{top:89px}.row-2{top:619px}.row-3{top:1149px}.row-4{top:1680px}.row-5{top:2209px}
.lead{font:700 26px/1.3 "Josefin Sans",sans-serif;text-transform:uppercase;letter-spacing:.5px}
.lead.lg{font-size:36px;line-height:1.2}
.punch{font:400 62px/1.12 "Anton",sans-serif;text-transform:uppercase;letter-spacing:-.5px}
.punch.md{font-size:50px}
.punch.sm{font-size:44px}
.rule{width:350px;height:5px;background:var(--white);border-radius:3px;margin:16px 0 18px;box-shadow:0 2px 3px rgba(120,20,70,.3)}
.pill{border:4px solid var(--white);border-radius:28px;padding:8px 24px 4px;margin-top:12px}
.bracket{position:relative;padding:4px 46px}
.bracket::before,.bracket::after{
  content:"";position:absolute;top:24px;bottom:24px;width:36px;border:4px solid var(--white);
}
.bracket::before{left:0;border-right:none;border-radius:14px 0 0 14px}
.bracket::after{right:0;border-left:none;border-radius:0 14px 14px 0}
.boxed{position:relative;border:4px solid var(--white);border-bottom:none;border-radius:14px 14px 0 0;padding:10px 36px 0}
.boxed::before,.boxed::after{content:"";position:absolute;bottom:-22px;width:36px;height:22px;border:4px solid var(--white);border-top:none}
.boxed::before{left:-4px;border-right:none;border-radius:0 0 0 14px}
.boxed::after{right:-4px;border-left:none;border-radius:0 0 14px 0}
.gap-s{margin-top:10px}.gap-m{margin-top:22px}
</style>
</head>
<body>
<main class="board">

  <section class="tile col-a row-1">
    <span class="tab"></span><span class="handle">@RKMarlowLive</span>
    <p class="lead">Struggling with</p>
    <h2 class="punch" style="font-size:70px;line-height:1.05">Bloating and<br>belly fat?</h2>
    <span class="rule"></span>
    <p class="lead">Try this natural<br>solution tonight, and<br>wake up feeling lighter !</p>
  </section>

  <section class="tile col-b row-1">
    <span class="tab"></span><span class="handle">@RKMarlowLive</span>
    <p class="lead lg">Wake up<br>tomorrow with<br>a flatter belly!<br>Yes, this<br>overnight remedy</p>
    <p class="lead lg pill">Works like magic!</p>
  </section>

  <section class="tile col-a row-2">
    <span class="tab"></span><span class="handle">@RKMarlowLive</span>
    <p class="lead lg" style="font-size:32px">Finally a natural<br>solution! That</p>
    <h2 class="punch md bracket gap-s" style="line-height:1.15">Flattens your<br>belly and eases<br>stomach bloat!</h2>
  </section>

  <section class="tile col-b row-2">
    <span class="tab"></span><span class="handle">@RKMarlowLive</span>
    <h2 class="punch sm boxed">One supplement</h2>
    <h2 class="punch" style="font-size:72px;line-height:1">One night</h2>
    <p class="lead gap-m" style="font-size:28px">Your belly bloat could<br>be gone by morning.<br>Here's how it works!</p>
  </section>

  <section class="tile col-a row-3">
    <span class="tab"></span><span class="handle">@RKMarlowLive</span>
    <h2 class="punch md">Sis, your hormones<br>are out of whack!</h2>
    <span class="rule" style="width:365px"></span>
    <p class="lead lg" style="font-size:32px">That's why the<br>weight won't budge!</p>
  </section>

  <section class="tile col-b row-3">
    <span class="tab"></span><span class="handle">@RKMarlowLive</span>
    <p class="lead" style="font-size:29px">GLP-1: The magic behind<br>the weight loss drugs.</p>
    <h2 class="punch sm gap-s" style="font-size:46px">But here's the secret!</h2>
    <span class="rule"></span>
    <p class="lead" style="font-size:30px">You can boost it<br>naturally without<br>a prescription!</p>
  </section>

  <section class="tile col-a row-4">
    <span class="tab"></span><span class="handle">@RKMarlowLive</span>
    <p class="lead">A natural way<br>to boost GLP-1 :</p>
    <h2 class="punch gap-s" style="font-size:58px;line-height:1.08">No injections<br>no side effects</h2>
    <span class="rule" style="width:375px"></span>
    <p class="lead" style="font-size:32px">Just real results.<br>Here's how it works</p>
  </section>

  <section class="tile col-b row-4">
    <span class="tab"></span><span class="handle">@RKMarlowLive</span>
    <p class="lead lg">You've been lied to</p>
    <p class="lead lg pill" style="border-radius:12px;padding:10px 14px 6px">'Just eat less and<br>exercise more'</p>
    <p class="lead lg gap-m">Doesn't work in<br>menopause</p>
  </section>

  <section class="tile col-a row-5">
    <span class="tab"></span><span class="handle">@RKMarlowLive</span>
    <p class="lead lg" style="font-size:40px;line-height:1.3">That stubborn<br>belly fat isn't<br>your fault!</p>
    <p class="lead pill" style="font-size:34px;border-radius:16px;padding:10px 26px 4px">Here's what no<br>one tells you.</p>
  </section>

  <section class="tile col-b row-5">
    <span class="tab"></span><span class="handle">@RKMarlowLive</span>
    <p class="lead" style="font-size:32px">Frustrated with</p>
    <h2 class="punch" style="font-size:66px;line-height:1.08">Belly fat that<br>wont budge?</h2>
    <span class="rule" style="width:365px"></span>
    <p class="lead" style="font-size:25px">I've got the solution that<br>finally worked for me<br>no crazy diets required!</p>
  </section>

</main>
</body>
</html>
```